Holloway Lane Grocer Business Cards
Holloway Lane Grocer
Holloway Lane Grocer Business Cards - Food
Creative Brief
Use specific fonts
Designer choice to compliment font used in logo
Professional
Melissa Carver
Store Manager
274 W Millrace Rd Alder Springs, NV 45912
melissa@hollowaylanegrocer.example
www.HollowayLaneGrocer.example

```html
<!DOCTYPE html>
<html lang="en">
<head>
<meta charset="utf-8">
<title>Holloway Lane Grocer – Business Card</title>
<link rel="stylesheet" href="https://fonts.googleapis.com/css2?family=Open+Sans:wght@400;600;700&display=swap">
<style>
  :root {
    --page-bg: #2b2b2b;
    --card-black: #0d0d0d;
    --card-white: #ffffff;
    --text-light: #f2f2f2;
    --text-muted: #d6d6d6;
    --divider: #8a8a8a;
    --icon-bg: #3a3a3a;
  }
  * { margin: 0; padding: 0; box-sizing: border-box; }
  html, body {
    width: 1200px; height: 911px; overflow: hidden;
    background: var(--page-bg);
    font-family: "Open Sans", Arial, sans-serif;
  }
  .business-card {
    position: absolute; left: 100px; top: 175px;
    width: 1000px; height: 560px;
    box-shadow: 0 18px 40px rgba(0,0,0,.55);
    overflow: hidden;
  }
  .card-shapes { position: absolute; inset: 0; }
  .brand {
    position: absolute; left: 50px; top: 115px; width: 360px;
    display: flex; flex-direction: column; align-items: center; gap: 18px;
  }
  .brand-dot {
    width: 64px; height: 64px; border-radius: 50%;
    background: var(--card-black);
  }
  .brand-name {
    font-weight: 600; font-size: 32px; line-height: 1.15;
    color: var(--card-black); text-align: center; text-transform: uppercase;
    letter-spacing: 1px;
  }
  .person {
    position: absolute; left: 600px; top: 185px; width: 300px;
    color: var(--text-light); text-align: center;
  }
  .person-name { font-weight: 700; font-size: 28px; }
  .person-role { font-weight: 400; font-size: 22px; margin-top: 14px; color: var(--text-muted); }
  .contact-strip {
    position: absolute; left: 0; right: 0; top: 452px; height: 108px;
    display: flex; align-items: center; padding: 0 30px;
    color: var(--text-light); font-size: 17px; line-height: 1.55;
    white-space: nowrap;
  }
  .contact-item { display: flex; align-items: center; gap: 12px; padding: 0 22px; }
  .contact-item + .contact-item { border-left: 1px solid var(--divider); }
  .contact-icon { width: 26px; height: 26px; flex: none; }
  .strong { font-weight: 700; }
</style>
</head>
<body>
  <div class="business-card">
    <svg class="card-shapes" width="1000" height="560" viewBox="0 0 1000 560" aria-hidden="true">
      <rect width="1000" height="560" fill="var(--card-black)"/>
      <path d="M0 0 H390 Q440 0 446 48 L472 432 H0 Z" fill="var(--card-white)"/>
      <line x1="472" y1="432" x2="1000" y2="420" stroke="var(--card-white)" stroke-width="3"/>
    </svg>

    <div class="brand">
      <div class="brand-dot"></div>
      <div class="brand-name">Holloway Lane Grocer</div>
    </div>

    <div class="person">
      <div class="person-name">Melissa Carver</div>
      <div class="person-role">Store Manager</div>
    </div>

    <div class="contact-strip">
      <div class="contact-item">
        <svg class="contact-icon" viewBox="0 0 26 26" aria-hidden="true">
          <circle cx="13" cy="13" r="12" fill="var(--icon-bg)"/>
          <path d="M9 7 l3 0 l1 4 l-2 1 q1 3 4 4 l1-2 l4 1 l0 3 q-9 1-11-11z" fill="var(--text-light)"/>
        </svg>
        <div>555-<span class="strong">555</span>-0186<br><span class="strong">555</span>-555-<span class="strong">0173</span></div>
      </div>
      <div class="contact-item">
        <svg class="contact-icon" viewBox="0 0 26 26" aria-hidden="true">
          <circle cx="13" cy="13" r="12" fill="var(--icon-bg)"/>
          <rect x="7" y="9" width="12" height="9" fill="none" stroke="var(--text-light)" stroke-width="1.6"/>
          <path d="M7 9 l6 5 l6-5" fill="none" stroke="var(--text-light)" stroke-width="1.6"/>
        </svg>
        <div>melissa@hollowaylanegrocer.example<br>www.HollowayLaneGrocer<span class="strong">.example</span></div>
      </div>
      <div class="contact-item">
        <svg class="contact-icon" viewBox="0 0 26 26" aria-hidden="true">
          <circle cx="13" cy="13" r="12" fill="var(--icon-bg)"/>
          <path d="M13 6 a5 5 0 0 1 5 5 c0 4-5 9-5 9 s-5-5-5-9 a5 5 0 0 1 5-5z" fill="var(--text-light)"/>
          <circle cx="13" cy="11" r="2" fill="var(--icon-bg)"/>
        </svg>
        <div><span class="strong">274 W</span> Millrace Rd<br>Alder Springs, NV 45912</div>
      </div>
    </div>
  </div>
</body>
</html>
```